Email Newsletter Banner

I require 2 new email newsletter and web banners to be made up.
I require the brand names to be included on the banner which are " Wire Dispatcher" and "PC Flashz". I would also like some sort of imagery and also a "sign up here" button. Please see below examples:
https://dataskyreports.lornexhub.com/
https://datawisdomsky.lornexhub.com/
https://datastoryvault.lornexhub.com/

```html
<!DOCTYPE html>
<html lang="en">
<head>
<meta charset="utf-8">
<title>Wire Dispatcher – Newsletter Banners</title>
<link rel="stylesheet" href="https://fonts.googleapis.com/css2?family=Orbitron:wght@700;900&family=Roboto+Slab:wght@700&display=swap">
<style>
  :root {
    --stage: #a6a6a6;
    --white: #ffffff;
    --button-ink: #26126b;
    --purple-dark: #4f2fb0;
    --purple-mid: #7350e0;
    --purple-light: #7d5cf2;
    --green-dark: #003a2a;
    --green-mid: #06a086;
    --green-light: #10b899;
    --blue-dark: #0b3a7c;
    --blue-mid: #1463c4;
    --blue-light: #1a72d6;
  }
  * { margin: 0; padding: 0; box-sizing: border-box; }
  html, body {
    width: 1200px;
    height: 763px;
    overflow: hidden;
    background: var(--stage);
  }
  .stage {
    position: relative;
    width: 1200px;
    height: 763px;
  }
  .banner {
    position: absolute;
    left: 24px;
    width: 1150px;
    height: 141px;
    overflow: hidden;
    box-shadow: 4px 6px 6px rgba(0, 0, 0, 0.45);
  }
  .banner--purple {
    top: 45px;
    background: linear-gradient(90deg, var(--purple-dark) 0%, var(--purple-mid) 45%, var(--purple-light) 100%);
  }
  .banner--green {
    top: 316px;
    background: linear-gradient(90deg, var(--green-dark) 0%, var(--green-mid) 45%, var(--green-light) 100%);
  }
  .banner--blue {
    top: 580px;
    background: linear-gradient(90deg, var(--blue-dark) 0%, var(--blue-mid) 45%, var(--blue-light) 100%);
  }
  .banner__globe {
    position: absolute;
    left: 511px;
    top: 70px;
    width: 102px;
    height: 102px;
    border-radius: 50%;
    background: radial-gradient(circle at 50% 30%, rgba(255,255,255,0.35) 0%, rgba(150,230,255,0.18) 45%, rgba(255,255,255,0.05) 75%);
    box-shadow: 0 -6px 22px rgba(255, 220, 255, 0.45);
  }
  .banner__brand {
    position: absolute;
    left: 27px;
    top: 40px;
    color: var(--white);
    font-family: 'Orbitron', sans-serif;
    font-weight: 900;
    font-size: 39px;
    line-height: 1;
    letter-spacing: 0.5px;
    text-transform: uppercase;
    white-space: nowrap;
  }
  .banner__tagline {
    position: absolute;
    left: 27px;
    top: 94px;
    color: var(--white);
    font-family: 'Orbitron', sans-serif;
    font-weight: 700;
    font-size: 11.5px;
    line-height: 1;
    letter-spacing: 2.3px;
    text-transform: uppercase;
    white-space: nowrap;
  }
  .banner__signup {
    position: absolute;
    left: 924px;
    top: 50px;
    width: 160px;
    height: 44px;
    display: flex;
    align-items: center;
    justify-content: center;
    background: var(--white);
    border-radius: 3px;
    color: var(--button-ink);
    font-family: 'Roboto Slab', serif;
    font-weight: 700;
    font-size: 17px;
    text-decoration: none;
    white-space: nowrap;
  }
</style>
</head>
<body>
<main class="stage">
  <section class="banner banner--purple">
    <div class="banner__globe" role="img" aria-label="Glowing wireframe globe illustration"></div>
    <h1 class="banner__brand">Wire Dispatcher</h1>
    <p class="banner__tagline">Essential whitepapers for IT professionals</p>
    <a class="banner__signup" href="#">SIGN UP HERE</a>
  </section>

  <section class="banner banner--green">
    <div class="banner__globe" role="img" aria-label="Glowing wireframe globe illustration"></div>
    <h1 class="banner__brand">Wire Dispatcher</h1>
    <p class="banner__tagline">Essential whitepapers for IT professionals</p>
    <a class="banner__signup" href="#">SIGN UP HERE</a>
  </section>

  <section class="banner banner--blue">
    <div class="banner__globe" role="img" aria-label="Glowing wireframe globe illustration"></div>
    <h1 class="banner__brand">Wire Dispatcher</h1>
    <p class="banner__tagline">Essential whitepapers for IT professionals</p>
    <a class="banner__signup" href="#">SIGN UP HERE</a>
  </section>
</main>
</body>
</html>
```